Quvanta Redesign

We need a face lift for our website, www.quvanta.com. We sell flooring and related products nationwide. We are interested in expanding the width of the website and introducing grays and black. We want the design to be both contemporary and user friendly.

```html
<!DOCTYPE html>
<html lang="en">
<head>
<meta charset="utf-8">
<title>Quvanta – Flooring</title>
<link href="https://fonts.googleapis.com/css2?family=Open+Sans:wght@400;600;700&display=swap" rel="stylesheet">
<style>
:root{
  --red:#e8141b;
  --black:#1f1f1f;
  --ink:#2b2b2b;
  --muted:#6b6b6b;
  --line:#d9d9d9;
  --page:#f1f1f1;
  --white:#ffffff;
}
*{box-sizing:border-box;margin:0;padding:0}
html,body{width:931px;height:1200px;overflow:hidden}
body{background:var(--page);font-family:"Open Sans",Arial,sans-serif;color:var(--ink);font-size:9px}
.canvas{position:relative;width:931px;height:1200px;overflow:hidden}
.abs{position:absolute}
.topbar{left:125px;top:0;width:681px;height:25px;background:var(--white);display:flex;align-items:center;padding:0 10px;font-size:9px}
.topbar .item{display:flex;align-items:center;gap:5px;margin-right:15px}
.topbar .right{margin-left:auto;display:flex;align-items:center;gap:18px}
.phone{color:var(--red);font-weight:700;font-size:12px;display:flex;align-items:center;gap:6px}
.logo{left:125px;top:40px;height:44px;display:flex;align-items:center;gap:6px}
.logo .mark{width:16px;height:16px;background:var(--red)}
.logo .name{font-size:26px;font-weight:700;color:var(--black);letter-spacing:-.5px}
.search{left:358px;top:51px;width:216px;height:24px;display:flex;border:1px solid var(--line);background:var(--white)}
.search span{flex:1;padding:5px 8px;color:#9a9a9a;font-size:8.5px}
.search b{width:26px;background:var(--black);display:flex;align-items:center;justify-content:center}
.cart{left:665px;top:51px;width:141px;height:24px;border:1px solid var(--line);background:var(--white);display:flex;align-items:center;justify-content:center;gap:5px;font-size:8.5px}
.cart em{font-style:normal;color:var(--red)}
.nav{left:125px;top:100px;width:681px;height:25px;background:var(--black);display:flex}
.nav a{color:var(--white);text-decoration:none;font-size:8.5px;display:flex;align-items:center;justify-content:center;border-right:1px solid #3a3a3a}
.nav a.active{background:var(--red)}
.hero{left:125px;top:139px;width:454px;height:236px;background:linear-gradient(180deg,#c89a68 0%,#9a5a2c 55%,#5e2e14 100%)}
.hero .dots{position:absolute;right:10px;top:22px;background:rgba(0,0,0,.55);padding:4px 6px;display:flex;gap:5px}
.hero .dots i{width:7px;height:7px;border-radius:50%;background:var(--white)}
.hero .dots i:first-child{background:var(--red)}
.hero .caption{position:absolute;left:0;bottom:20px;background:rgba(40,40,40,.82);color:var(--white);font-size:16.5px;padding:4px 16px;letter-spacing:.5px}
.promo{left:597px;width:209px;background:var(--white);border:1px solid var(--line)}
.promo.sale{top:139px;height:110px}
.promo.sale .art{position:absolute;left:0;top:0;width:70px;height:84px;background:linear-gradient(160deg,#e7d3a0,#a8201c)}
.promo.sale h3{position:absolute;left:84px;top:6px;font-size:19px;font-weight:400;color:var(--red);line-height:1.2}
.promo.sale h3 b{display:block;color:var(--black);font-weight:700;font-size:22px}
.promo.sale .btn{position:absolute;left:85px;top:60px;background:var(--red);color:var(--white);font-size:8px;font-weight:700;padding:2px 8px}
.promo.sale .strip{position:absolute;left:0;bottom:0;width:100%;height:24px;background:var(--black);color:var(--white);font-size:10px;display:flex;align-items:center;justify-content:center}
.promo.free{top:265px;height:110px}
.promo.free h3{position:absolute;left:12px;top:8px;font-size:24px;font-weight:400;color:var(--black)}
.promo.free h3 b{color:var(--red)}
.promo.free p{position:absolute;left:12px;top:50px;font-size:9px;line-height:1.3;color:var(--black)}
.promo.free .art{position:absolute;right:0;bottom:0;width:90px;height:62px;background:linear-gradient(135deg,#d9a24a,#8b3a2a 60%,#4a6a3a)}
.side{left:125px;width:163px;background:var(--white);border:1px solid var(--line)}
.side h4{height:25px;border-left:3px solid var(--red);border-bottom:1px solid var(--line);font-weight:400;font-size:12.5px;padding:3px 0 0 8px;background:var(--white)}
.side ul{list-style:none;padding:4px 0}
.side li{height:22px;margin:0 1px;border-bottom:1px dotted var(--line);display:flex;align-items:center;justify-content:space-between;padding:0 10px;font-size:8.5px;color:#555}
.side li span{color:#555;font-size:10px}
.side li:last-child{border-bottom:none}
.side li.active,.side li.active span{background:var(--black);color:var(--white)}
.side ul.top{padding-top:5px}
.section-head{left:309px;width:497px;height:30px;border-bottom:1px solid var(--line)}
.section-head h2{font-size:17px;font-weight:400;color:var(--black)}
.section-head h2 span{color:var(--red);font-size:19px}
.section-head p{font-size:9px;color:var(--muted);margin-top:-2px}
.section-head .tag{position:absolute;right:0;top:0;background:var(--red);color:var(--white);font-size:9px;padding:5px 10px}
.tile{width:156px;height:124px;background:var(--white);border:1px solid var(--line)}
.tile .ph{height:99px}
.tile .lbl{height:25px;display:flex;align-items:center;justify-content:center;font-size:10px;color:var(--black)}
.tile.active .lbl{background:var(--black);color:var(--white)}
.arrow{top:830px}
.product{width:143px}
.product .ph{height:104px}
.product .brand{margin-top:6px;font-size:10px;color:var(--black);padding-left:3px}
.product .desc{font-size:8.5px;color:var(--muted);padding-left:3px;white-space:nowrap}
.product .price{margin-top:8px;font-size:8.5px;color:var(--muted);padding-left:3px}
.product .price b{color:var(--red);font-size:12px}
.legal{left:125px;top:1003px;width:681px;height:33px;background:var(--black);color:var(--white);font-size:7.5px;text-align:center;padding-top:6px;line-height:1.3}
.footer{left:125px;top:1036px;width:681px;height:164px;background:var(--white)}
.links{position:absolute;top:18px;list-style:none;font-size:8.5px;line-height:12.3px;color:var(--black)}
.links li.red{color:var(--red)}
.newsletter{position:absolute;left:276px;top:18px}
.newsletter h5{font-size:11px;font-weight:600}
.newsletter .field{margin-top:6px;width:137px;height:24px;border:1px solid var(--line);font-size:8.5px;color:#9a9a9a;padding:5px 7px}
.newsletter .join{margin-top:8px;display:inline-block;background:var(--black);color:var(--white);font-size:8.5px;padding:4px 10px;border-radius:2px}
.badge{position:absolute;background:#e3e3e3}
.rule{position:absolute;left:0;top:111px;width:681px;height:1px;background:var(--line)}
.pay{position:absolute;top:130px;width:28px;height:18px;background:#dde3ec;border-radius:2px}
.social{position:absolute;top:128px;width:20px;height:20px}
</style>
</head>
<body>
<div class="canvas">

  <div class="abs topbar">
    <span class="item">
      <svg width="11" height="11" viewBox="0 0 11 11"><rect x="2" y="1" width="7" height="9" fill="none" stroke="#444"/><path d="M4 4h3M4 6h3" stroke="#444"/></svg>Order Tracking</span>
    <span class="item">
      <svg width="11" height="11" viewBox="0 0 11 11"><circle cx="5.5" cy="5.5" r="4.5" fill="none" stroke="#444"/><text x="3.6" y="8" font-size="7" fill="#444" font-family="Arial">?</text></svg>FAQ</span>
    <span class="item">
      <svg width="11" height="11" viewBox="0 0 11 11"><circle cx="5.5" cy="3" r="2.2" fill="#666"/><path d="M1.5 11c0-4 8-4 8 0z" fill="#666"/></svg>My Account</span>
    <div class="right">
      <span class="phone">
        <svg width="13" height="11" viewBox="0 0 13 11"><path d="M1 4c3-3 8-3 11 0l-2 1.5-1-1.5H4L3 5.5z" fill="#444"/><rect x="3" y="6" width="7" height="4" fill="#444"/></svg>1-888-555-0142</span>
      <span class="item" style="margin-right:0">
        <svg width="12" height="11" viewBox="0 0 12 11"><path d="M1 5c0-3 10-3 10 0s-6 3-7 2l-3 2 1-3z" fill="#444"/></svg>LIVE CHAT</span>
    </div>
  </div>

  <div class="abs logo"><span class="mark"></span><span class="name">Quvanta</span></div>

  <div class="abs search"><span>Description or Items</span><b>
    <svg width="12" height="12" viewBox="0 0 12 12"><circle cx="5" cy="5" r="3.5" fill="none" stroke="#fff" stroke-width="1.8"/><path d="M7.5 7.5l3 3" stroke="#fff" stroke-width="2"/></svg></b></div>

  <div class="abs cart">
    <svg width="14" height="12" viewBox="0 0 14 12"><path d="M1 1h2l2 7h7l1.5-5H4" fill="none" stroke="#444"/><circle cx="6" cy="10.5" r="1" fill="#444"/><circle cx="11" cy="10.5" r="1" fill="#444"/></svg>
    MY CART : <em>0 PRODUCT (S)</em></div>

  <nav class="abs nav">
    <a class="active" style="width:71px">LAMINATE</a>
    <a style="width:77px">HARDWOOD</a>
    <a style="width:73px">AREA RUGS</a>
    <a style="width:62px">BAMBOO</a>
    <a style="width:46px">CORK</a>
    <a style="width:50px">VINYL</a>
    <a style="width:80px">CARPET TILE</a>
    <a style="width:33px">TILE</a>
    <a style="width:59px">CLOCKS</a>
    <a style="width:47px">BATH</a>
    <a style="width:83px;border-right:none">CLEARANCE</a>
  </nav>

  <div class="abs hero" role="img" aria-label="Kitchen with warm wood cabinets, round glass table and dark hardwood floor">
    <div class="dots"><i></i><i></i><i></i><i></i></div>
    <div class="caption">BEST <b>FLOORING</b> SERVICES</div>
  </div>

  <div class="abs promo sale">
    <div class="art" role="img" aria-label="Celebration bottle and glasses"></div>
    <h3>NEW YEAR<b>SALE !</b></h3>
    <span class="btn">Know More</span>
    <div class="strip"><b>FREE SHIPPING</b>&nbsp;ONE DAY ONLY !</div>
  </div>

  <div class="abs promo free">
    <h3><b>FREE</b> SAMPLES</h3>
    <p>COMPLETELY FREE,<br>NO CEDIT CARD<br>REQUIRED</p>
    <div class="art" role="img" aria-label="Fanned stack of colorful flooring samples"></div>
  </div>

  <aside class="abs side" style="top:393px;height:188px">
    <h4>Our Brands</h4>
    <ul class="top">
      <li class="active">LAMINATE<span>»</span></li>
      <li>HARDWOOD<span>»</span></li>
      <li>BAMBOO<span>»</span></li>
      <li>CORK<span>»</span></li>
      <li>VINYL<span>»</span></li>
      <li>CARPET TILE<span>»</span></li>
      <li>TILE<span>»</span></li>
    </ul>
  </aside>

  <aside class="abs side" style="top:598px;height:101px">
    <h4>Home Decor</h4>
    <ul>
      <li>AREA RUGS<span>»</span></li>
      <li>BATH<span>»</span></li>
      <li>CLOCKS<span>»</span></li>
    </ul>
  </aside>

  <aside class="abs side" style="top:717px;height:124px">
    <h4>Accessories</h4>
    <ul>
      <li>UNDERLAYMENT<span>»</span></li>
      <li>TRIM &amp; MOLDING<span>»</span></li>
      <li>FLOOR CLEANER<span>»</span></li>
      <li>INSTALLATION TOOLS<span>»</span></li>
    </ul>
  </aside>

  <aside class="abs side" style="top:858px;height:125px">
    <h4>Flooring Facts</h4>
    <ul>
      <li>LAMINATE<span>»</span></li>
      <li>HARDWOOD<span>»</span></li>
      <li>CORK<span>»</span></li>
      <li>AREA RUGS<span>»</span></li>
    </ul>
  </aside>

  <div class="abs section-head" style="top:393px;height:45px">
    <h2><span>S</span>pecial <span>O</span>fferings</h2>
    <p>From the brands you know and trust.</p>
    <span class="tag" style="top:10px">CURRENT PROMITIONS</span>
  </div>

  <div class="abs tile active" style="left:309px;top:455px"><div class="ph" role="img" aria-label="Living room with light laminate floor and black sofa" style="background:linear-gradient(180deg,#6a8f9a,#c7b8a5 60%,#a88d70)"></div><div class="lbl">Laminate</div></div>
  <div class="abs tile" style="left:479px;top:455px"><div class="ph" role="img" aria-label="Dining room with warm hardwood floor and patterned rug" style="background:linear-gradient(180deg,#b8862e,#8a4a1a 60%,#6b2f12)"></div><div class="lbl">Hardwood</div></div>
  <div class="abs tile" style="left:650px;top:455px"><div class="ph" role="img" aria-label="Bright room with cork floor and white sofa" style="background:linear-gradient(180deg,#e2d6cc,#c8a58a 55%,#9a5a2a)"></div><div class="lbl">Cork</div></div>
  <div class="abs tile" style="left:309px;top:595px"><div class="ph" role="img" aria-label="Room with fireplace and pale bamboo floor" style="background:linear-gradient(180deg,#4a3a2a,#8a7050 50%,#d9c49a)"></div><div class="lbl">Bamboo</div></div>
  <div class="abs tile" style="left:479px;top:595px"><div class="ph" role="img" aria-label="Lounge with black sofa on striped orange vinyl floor" style="background:linear-gradient(180deg,#d8d4cc,#e9e0d2 50%,#d47c3c)"></div><div class="lbl">Vinyl</div></div>
  <div class="abs tile" style="left:650px;top:595px"><div class="ph" role="img" aria-label="Orange room with armchair and area rug" style="background:linear-gradient(180deg,#c2502a,#8a3a20 55%,#d8c8b8)"></div><div class="lbl">Area Rugs</div></div>

  <div class="abs section-head" style="top:741px;height:32px">
    <h2 style="margin-top:3px"><span>F</span>eatured <span>P</span>roducts</h2>
    <span class="tag">VIEW ALL</span>
  </div>

  <svg class="abs arrow" style="left:309px" width="8" height="40" viewBox="0 0 8 40"><path d="M7 1L1 20l6 19" fill="none" stroke="#555"/></svg>
  <svg class="abs arrow" style="left:799px" width="8" height="40" viewBox="0 0 8 40"><path d="M1 1l6 19-6 19" fill="none" stroke="#555"/></svg>

  <div class="abs product" style="left:327px;top:793px">
    <div class="ph" role="img" aria-label="Room with stone fireplace and honey laminate floor" style="background:linear-gradient(180deg,#8a7060,#c08a5a 50%,#a8683a)"></div>
    <div class="brand">Northvale</div><div class="desc">Shoreline Haven 12mm Laminate</div>
    <div class="price">Starting at <b>$2.49</b> Sq. Ft.</div>
  </div>
  <div class="abs product" style="left:487px;top:793px">
    <div class="ph" role="img" aria-label="Glossy wood-look vinyl tile floor" style="background:linear-gradient(180deg,#9a6a3a,#c8925a 50%,#8a5a2a)"></div>
    <div class="brand">Corvell</div><div class="desc">Terralux Luxury Vinyl Tile</div>
    <div class="price">Starting at <b>$3.79</b> Sq. Ft.</div>
  </div>
  <div class="abs product" style="left:646px;top:793px">
    <div class="ph" role="img" aria-label="Acacia hardwood floor with round orange table" style="background:linear-gradient(180deg,#c8702a,#c48850 50%,#a8703a)"></div>
    <div class="brand">Northvale</div><div class="desc">Timber Hollow Acacia Hardwood</div>
    <div class="price">Starting at <b>$4.99</b> Sq. Ft.</div>
  </div>

  <div class="abs legal">©1999-2013 Brightline Home Goods, Inc. All rights reserved. <b>QUVANTA</b>, <b>QUVANTA</b> OUTLET, and <b>QUVANTA.COM</b> are trademarks of<br>Brightline Home Goods, Inc. or its affiliates.</div>

  <footer class="abs footer">
    <ul class="links" style="left:14px">
      <li class="red">About us</li><li>Careers</li><li>Consumer reviews</li><li>Contact us</li><li>Faq</li>
    </ul>
    <ul class="links" style="left:151px">
      <li>Ordering</li><li>Pricing</li><li>Privacy policy</li><li>Return policy</li><li>Shipping</li><li>Sitemap</li>
    </ul>
    <div class="newsletter">
      <h5>Newsletter</h5>
      <div class="field">Enter your Email ...</div>
      <span class="join">JOIN</span>
    </div>
    <div class="badge" style="left:458px;top:22px;width:48px;height:28px;border-radius:3px"></div>
    <div class="badge" style="left:523px;top:24px;width:85px;height:24px;border-radius:3px"></div>
    <div class="badge" style="left:623px;top:15px;width:38px;height:38px;border-radius:50%;background:#e6d99a"></div>
    <div class="rule"></div>
    <div class="badge" style="left:14px;top:122px;width:32px;height:32px;border-radius:50%;background:#e6d99a"></div>
    <div style="position:absolute;left:59px;top:121px;width:1px;height:34px;background:var(--line)"></div>
    <div class="pay" style="left:72px"></div>
    <div class="pay" style="left:106px"></div>
    <div class="pay" style="left:139px"></div>
    <div class="pay" style="left:172px"></div>
    <div class="pay" style="left:205px"></div>
    <div class="pay" style="left:238px"></div>
    <div class="social" style="left:572px;background:var(--red)"></div>
    <div class="social" style="left:597px;background:var(--black)"></div>
    <div class="social" style="left:622px;background:var(--black)"></div>
    <div class="social" style="left:647px;background:var(--black)"></div>
  </footer>

</div>
</body>
</html>
```